Poster for a 100 y.o. Tennis Tournament

I would like a poster designed to promote our tennis tournament but I'd like to avoid some of the clichés like the shadow of a player serving. Just well styled text would be fine but some clever imagery would be a bonus.
Highlighting the fact our tournament has been running for over 100 years would be nice so a retro design would work. But that doesn't mean a modern design, for example a minimalist approach utilising the lines of a tennis court, wouldn't work.
Updates

Our tennis committee is now in the process of short listing and will provide an update within 48 hours.

Industry/Entity Type

Court

Requirements
Must have
• The poster must contain the following text at a minimum:
"Marbury Tennis Tournament"/"Since 1908"
"9 March - 11 March, 2013" or "9-11 March, 2013", etc
"www.marburytennis.com.au"

The poster must be reproducible in colour and black & white, or at least have an alternate for black & white.

The poster must be usable in both A3 and A4 sizes.
Nice to have
• The poster should contain the following text:
"Championship"
"Handicap"
"Seniors"
"Juniors"
Each above may be optionally succeeded by "Singles & Doubles", e.g. "Championship Singles & Doubles". It would actually be clearer if this additional text was used but would be repetitive, so alternate text "Singles & Doubles in all categories" might also be used. Alternatives for variety (with the first word the focus): "Championship Singles & Doubles", "Handicap Singles & Doubles", "Seniors 35+ & 50+", "Juniors 18&U, 14&U"

Ideally the poster will provision room for four to eight sponsors logos, preferably at the bottom, but failure to do this is not a show stopper.

The following text may also be used:
"Entries close February 24"
"Tollard Plate Weekend"

Attached is a photo of one of the old trophies. Utilisation of the curved style of the "Marbury Tennis Tournament" text would fit in with the history if the tournament.

The ability to reuse elements of the poster in a single page website used to promote the tournament would be an advantage (as it will provide consistency).

If you could have an image of a tennis ball that conveys the same energy as the clock/tyre image in the attached "Under the Glass Moon" poster, that would be cool. Or using split imagery of a wooden racquet and a modern racquet, but with some energy, would also be good. These are just ideas though and by no means essential.

I've also attached a photo of a t-shirt with a poster layout I thought looked good.

Some additional text that can be used:
"Brand new courts"
"Brindle Park, Oakhurst Tce, Marbury"
"Phone 0427 318 642"
"Prizes and Trophies"

```html
<!DOCTYPE html>
<html lang="en">
<head>
<meta charset="utf-8">
<title>Marbury Tennis Tournament</title>
<link rel="stylesheet" href="https://fonts.googleapis.com/css2?family=Black+Ops+One&family=Pinyon+Script&display=swap">
<style>
  :root {
    --paper: #e9e0c9;
    --paper-edge: #c9bb98;
    --title-brown: #7d6d68;
    --title-blue: #6f9dc0;
    --ink: #262220;
    --date-brown: #7a6a64;
    --old-ball: #6e5443;
    --old-ball-dark: #3f2e25;
    --new-ball: #e4f03a;
    --new-ball-dark: #b9c51c;
    --stencil: "Black Ops One", sans-serif;
    --script: "Pinyon Script", cursive;
  }
  html, body {
    margin: 0;
    padding: 0;
    overflow: hidden;
    background: var(--paper);
  }
  .poster {
    width: 848px;
    height: 1200px;
    position: relative;
    overflow: hidden;
    background: radial-gradient(ellipse at 50% 45%, var(--paper) 55%, var(--paper-edge) 100%);
  }
  .poster svg { display: block; }
  .title { font-family: var(--stencil); }
  .title-town { fill: var(--title-brown); }
  .title-sport, .title-event { fill: var(--title-blue); }
  .since { font-family: var(--script); fill: var(--ink); font-size: 78px; }
  .date { font-family: var(--stencil); fill: var(--date-brown); font-size: 44px; }
  .format-label { font-family: var(--stencil); fill: var(--date-brown); font-size: 17px; }
  .category { font-family: var(--stencil); fill: var(--title-blue); font-size: 40px; }
  .web { font-family: var(--stencil); fill: var(--date-brown); font-size: 24px; }
</style>
</head>
<body>
<main class="poster">
  <svg width="848" height="1200" viewBox="0 0 848 1200">
    <defs>
      <radialGradient id="old-ball-tone" cx="40%" cy="35%" r="70%">
        <stop offset="0" stop-color="var(--old-ball)"/>
        <stop offset="1" stop-color="var(--old-ball-dark)"/>
      </radialGradient>
      <radialGradient id="new-ball-tone" cx="40%" cy="35%" r="70%">
        <stop offset="0" stop-color="var(--new-ball)"/>
        <stop offset="1" stop-color="var(--new-ball-dark)"/>
      </radialGradient>
    </defs>

    <g class="title">
      <text class="title-town" x="48" y="94" font-size="86" textLength="744" lengthAdjust="spacingAndGlyphs">MARBURY</text>
      <text class="title-sport" x="48" y="204" font-size="112" textLength="744" lengthAdjust="spacingAndGlyphs">TENNIS</text>
      <text class="title-event" x="48" y="282" font-size="76" textLength="744" lengthAdjust="spacingAndGlyphs">TOURNAMENT</text>
    </g>

    <circle class="old-ball" cx="264" cy="546" r="210" fill="url(#old-ball-tone)" role="img" aria-label="Worn vintage leather tennis ball"/>
    <circle class="new-ball" cx="552" cy="708" r="242" fill="url(#new-ball-tone)" role="img" aria-label="Bright modern yellow tennis ball"/>

    <text class="since" x="478" y="444" transform="rotate(-8 620 420)">Since1908</text>

    <g class="event-date">
      <text class="date" x="52" y="1024" textLength="150" lengthAdjust="spacingAndGlyphs">9-11</text>
      <text class="date" x="52" y="1066" textLength="150" lengthAdjust="spacingAndGlyphs">MAR</text>
      <text class="date" x="52" y="1108" textLength="150" lengthAdjust="spacingAndGlyphs">2013</text>
    </g>

    <g class="format-label" transform="rotate(-90 0 0)">
      <text class="format-label" x="-1110" y="224" textLength="124" lengthAdjust="spacingAndGlyphs">SINGLES &amp;</text>
      <text class="format-label" x="-1110" y="242" textLength="124" lengthAdjust="spacingAndGlyphs">DOUBLES:</text>
    </g>

    <g class="categories">
      <text class="category" x="250" y="1024" textLength="540" lengthAdjust="spacingAndGlyphs">CHAMPIONSHIP/HANDICAP</text>
      <text class="category" x="250" y="1066" textLength="540" lengthAdjust="spacingAndGlyphs">JUNIORS (under19s/under15s)</text>
      <text class="category" x="250" y="1108" textLength="540" lengthAdjust="spacingAndGlyphs">SENIORS (over35s/over50s)</text>
    </g>

    <text class="web" x="426" y="1160" textLength="366" lengthAdjust="spacingAndGlyphs">www.marburytennis.com.au</text>
  </svg>
</main>
</body>
</html>
```